Chorkonzert Thema Die KlangFalter fällt aus dem Rahmen
Zielgruppe
Wir sind ein A-Capella Chor 'KlangFalter'. Wir wollen Jung und Alt ansprechen.
Es sollen Plakate (30x42 cm) und Handzettel erstellt werden.
Aufgabenstellung
Wir sind noch völlig offen. Beim letzten Konzert wurde ein Foto (mit allen verwendet)
Entweder könnte wieder ein Foto mitverarbeitet werden. Wir laden mal zwei drei Fotos hoch. Von den Einzelstimmen sind jeweils Bilder noch vorhanden. Würden aber auch spezielle Fotos machen lassen je nachdem.
Gerne ein Plakat das entsprechend dem Konzerttitel etwas aus dem Rahmen fällt.
Text:
Wann: 10. und 12.03.2017 um ? Uhr
Eintritt: 8 Euro VVK 10 Euro AK
Kartenbestellung

```html
<!DOCTYPE html>
<html lang="de">
<head>
<meta charset="utf-8">
<title>KlangFalter – Acapella Chor</title>
<link href="https://fonts.googleapis.com/css2?family=Josefin+Sans:wght@700&display=swap" rel="stylesheet">
<style>
  :root {
    --skin-light: #f2c9c2;
    --skin-mid: #e2a39b;
    --skin-deep: #b87068;
    --hair: #d9cbb0;
    --text: #ffffff;
    --shadow: rgba(90, 60, 55, 0.55);
  }
  html, body {
    margin: 0;
    padding: 0;
    overflow: hidden;
    background: #ffffff;
  }
  .poster {
    position: relative;
    width: 856px;
    height: 1200px;
    overflow: hidden;
    font-family: "Josefin Sans", "Century Gothic", sans-serif;
    font-weight: 700;
    text-transform: uppercase;
    color: var(--text);
  }
  .poster__photo {
    position: absolute;
    inset: 0;
    background:
      radial-gradient(ellipse 40% 30% at 30% 58%, var(--skin-deep) 0%, rgba(184,112,104,0) 70%),
      radial-gradient(ellipse 60% 55% at 55% 40%, var(--skin-mid) 0%, rgba(226,163,155,0) 75%),
      radial-gradient(ellipse 35% 60% at 95% 25%, var(--hair) 0%, rgba(217,203,176,0) 80%),
      radial-gradient(ellipse 60% 20% at 40% 0%, var(--hair) 0%, rgba(217,203,176,0) 90%),
      linear-gradient(160deg, var(--skin-light) 0%, var(--skin-mid) 55%, var(--skin-light) 100%);
  }
  .line {
    position: absolute;
    right: 51px;
    margin: 0;
    text-align: right;
    white-space: nowrap;
    line-height: 1;
    text-shadow: 2px 3px 0 var(--shadow);
  }
  .choir-name { top: 296px; font-size: 86px; letter-spacing: 1px; }
  .choir-type { top: 432px; font-size: 58px; letter-spacing: 1px; }
  .event-dates { top: 846px; font-size: 64px; }
  .event-time { top: 918px; font-size: 32px; }
  .event-venue { top: 1010px; font-size: 42px; }
  .event-prices { top: 1068px; font-size: 42px; }
  .ticket-order {
    left: 52px;
    top: 1140px;
    font-size: 20px;
    letter-spacing: 0.5px;
    display: flex;
    justify-content: space-between;
    text-shadow: 1px 2px 0 var(--shadow);
  }
</style>
</head>
<body>
  <main class="poster">
    <div class="poster__photo" role="img" aria-label="Nahaufnahme eines Ohres, umrahmt von blondem Haar"></div>

    <h1 class="line choir-name">KlangFalter</h1>
    <p class="line choir-type">Acapella Chor</p>

    <p class="line event-dates">10.+12.03.2017</p>
    <p class="line event-time">20.00h</p>

    <p class="line event-venue">Aula Lindenhofgymnasium</p>
    <p class="line event-prices">Karten: VVK 8 €, AK 10 €</p>

    <p class="line ticket-order"><span>Kartenbestellung 07311 - 48210</span><span>josefine.br@post.de</span></p>
  </main>
</body>
</html>
```